Creative Consulting Company
business card, stationary, ppt template
Creative Consulting Company - Communications and Media
Creative Brief
Use specific fonts
Use what works the best in your design
Professional
Till Molnar
CEO
Molnar Communications GmbH Tannwaldstrasse 87 CH-8999 Zurich
till.molnar@molnarkom-demo.ch
www.molnarkom-demo.ch
Molnar Communications is a consultancy that specializes in all aspects of high end event organization and sponsorship activation. We are located in Switzerland. I'm looking for a clean and stylish look. The sizes are european: Letterhead: DIN A4 210mm x 297mm (8.27" x 11.69") Business Cards: 85mm x 54mm (3.346" x 2.126") Plz use "Mobile" instead of "Cell" Stationery: --------------- Do not use Ilustration which runs off the edge. We do print the letters with our own printers. Therefore, there will be a margin. And please no watermarks. Business Cards: ----------------------- I consider to grade up the back of the card with some varnish or film, but not sure yet. You can use either the black or the white logo. ppt Template: ------------------ Template should match the grafical concept.
Just the Logo. I you mind pimp up the logo a little bit (gradient, shadow, 3D etc.), feel free to do so. But you don't have to.

```html
<!DOCTYPE html>
<html lang="en">
<head>
<meta charset="utf-8">
<title>Molnar Communications – Business Cards</title>
<link href="https://fonts.googleapis.com/css2?family=Questrial&display=swap" rel="stylesheet">
<style>
  :root {
    --backdrop: #ebe7e1;
    --card-white: #ffffff;
    --card-dark: #4a4a4c;
    --ink: #3a3a3c;
    --ink-soft: #6b6b6e;
    --band: #1e1e20;
    --band-block: #d9d9db;
    --ghost-light: #ececec;
    --ghost-dark: #565658;
    --white: #ffffff;
  }
  * { margin: 0; padding: 0; box-sizing: border-box; }
  html, body {
    width: 1200px; height: 929px; overflow: hidden;
    background: var(--backdrop);
    font-family: "Questrial", "Century Gothic", sans-serif;
    color: var(--ink);
  }
  .canvas { position: relative; width: 1200px; height: 929px; }

  .card {
    position: absolute; width: 432px; height: 262px;
    border-radius: 16px; overflow: hidden;
    box-shadow: 0 6px 16px rgba(0,0,0,.18);
  }
  .card--front { left: 412px; top: 160px; background: var(--card-white); }
  .card--dark  { left: 196px; top: 428px; background: var(--card-dark); }
  .card--plain { left: 640px; top: 428px; background: var(--card-white); }

  .ghost-ring { position: absolute; }

  .brand { position: absolute; display: flex; flex-direction: column; align-items: center; gap: 6px; }
  .brand__dot { width: 38px; height: 38px; border-radius: 50%; border: 5px solid currentColor; }
  .brand__name { font-size: 20px; letter-spacing: 6px; line-height: 1; padding-left: 6px; }

  .card--front .brand { left: 50%; top: 18px; transform: translateX(-50%); color: var(--ink); }

  .contact {
    position: absolute; left: 12px; top: 108px;
    border-left: 3px solid var(--ink); padding-left: 8px;
    font-size: 11.5px; line-height: 15px; color: var(--ink);
  }
  .contact__company { font-size: 12px; }
  .contact__label { display: inline-block; width: 40px; color: var(--ink-soft); }

  .person { position: absolute; left: 284px; top: 108px; font-size: 12px; line-height: 15px; }
  .person__role { font-size: 10px; color: var(--ink-soft); }

  .band {
    position: absolute; left: 0; right: 0; bottom: 20px; height: 22px;
    background: var(--band);
  }
  .band__url {
    position: absolute; left: 112px; top: 4px;
    font-size: 11.5px; color: var(--white);
  }
  .band__block { position: absolute; top: 4px; width: 28px; height: 18px; background: var(--band-block); }
  .band__block--a { left: 302px; }
  .band__block--b { left: 342px; }

  .card--dark .brand { left: 70px; top: 76px; color: var(--white); }
  .card--dark .brand__dot { width: 52px; height: 52px; border-width: 6px; }
  .card--dark .brand__name { font-size: 22px; }
  .card--dark .url { color: var(--white); }

  .card--plain .brand { left: 50%; top: 90px; transform: translateX(-50%); color: var(--ink); }
  .card--plain .brand__dot { width: 64px; height: 64px; border-width: 7px; }

  .url { position: absolute; bottom: 16px; font-size: 12px; color: var(--ink); }
  .card--dark .url { left: 104px; }
  .card--plain .url { left: 130px; }
</style>
</head>
<body>
<main class="canvas">

  <section class="card card--front" aria-label="Business card front">
    <svg class="ghost-ring" style="left:268px;top:80px" width="140" height="140" viewBox="0 0 140 140" aria-hidden="true">
      <circle cx="70" cy="70" r="60" fill="none" stroke="var(--ghost-light)" stroke-width="14"/>
    </svg>
    <div class="brand">
      <span class="brand__dot"></span>
      <span class="brand__name">MOLNAR</span>
    </div>
    <div class="contact">
      <div class="contact__company">Molnar Communications GmbH</div>
      <div>Tannwaldstrasse 87</div>
      <div>CH-8999 Zurich</div>
      <div><span class="contact__label">Mobile :</span>+41 79 000 12 34</div>
      <div><span class="contact__label">Email :</span>till.molnar@molnarkom-demo.ch</div>
    </div>
    <div class="person">
      <div>Till Molnar</div>
      <div class="person__role">CEO</div>
    </div>
    <div class="band">
      <span class="band__url">www.molnarkom-demo.ch</span>
      <span class="band__block band__block--a"></span>
      <span class="band__block band__block--b"></span>
    </div>
  </section>

  <section class="card card--dark" aria-label="Business card back, dark">
    <svg class="ghost-ring" style="left:262px;top:70px" width="150" height="150" viewBox="0 0 150 150" aria-hidden="true">
      <circle cx="75" cy="75" r="64" fill="none" stroke="var(--ghost-dark)" stroke-width="16"/>
    </svg>
    <div class="brand">
      <span class="brand__dot"></span>
      <span class="brand__name">MOLNAR</span>
    </div>
    <span class="url">www.molnarkom-demo.ch</span>
  </section>

  <section class="card card--plain" aria-label="Business card back, white">
    <svg class="ghost-ring" style="left:278px;top:66px" width="150" height="150" viewBox="0 0 150 150" aria-hidden="true">
      <circle cx="75" cy="75" r="64" fill="none" stroke="var(--ghost-light)" stroke-width="16"/>
    </svg>
    <div class="brand">
      <span class="brand__dot"></span>
    </div>
    <span class="url">www.molnarkom-demo.ch</span>
  </section>

</main>
</body>
</html>
```